Specialized instructional design consultant needs a business card

**Hi Designers,
This project is put on hold until the logo project is completed. We will re-open this project at that time, if you are interested in the logo project see following link
http://jobs.pixelbazaar.example/job.aspx?id=472615

I need a business card that makes me stand out as an innovative, specialized professional that organizations can trust to lead their team through a project. I develop customized learning for the workflow - so my work is about being able to connect with my clients and their teams quickly and build their trust so we can develop the right solution. I like primary colours, designs that represent connections and movement. The final design should be clean, concise ... and cool.

Here are the details:

Company name is in the logo

Helen Marsh, B.Sc., M.Ed., PMP
helen.marsh@quillpond.example

Ryan Marsh, MBA
ryan.marsh@quillpond.example

Location:
Victoria, British Columbia
Canada

Phone:
250.555.0184

Reason: I needed to delay the start of this project because my logo wasn't done. Now it is done so we can move forward.

Target Market(s)

Executives who have the authority to make decisions about whether or not to hire me as a consultant on their team

Industry/Entity Type

Business

Font styles to use
Sans Serif

Requirements
Must have
• Clean, concise, but stands out
keep it simple
depicts connections between individual parts
primary colours
Nice to have
• a sense of movement / flow

```html
<!DOCTYPE html>
<html lang="en">
<head>
<meta charset="utf-8">
<title>Quill Pond Consulting — Business Card</title>
<link rel="stylesheet" href="https://fonts.googleapis.com/css2?family=PT+Sans:wght@400;700&display=swap">
<style>
  :root {
    --bg: #e4e1dd;
    --card: #ffffff;
    --ink-grey: #6f6f6f;
    --maroon: #7e1a10;
    --maroon-deep: #4e0e09;
    --gold: #f2a23a;
    --white: #ffffff;
  }
  * { margin: 0; padding: 0; box-sizing: border-box; }
  html, body {
    width: 1200px; height: 997px; overflow: hidden;
    background: var(--bg);
    font-family: "PT Sans", sans-serif;
  }
  .canvas { position: relative; width: 1200px; height: 997px; }
  .card {
    position: absolute; left: 280px;
    width: 640px; height: 366px;
    background: var(--card);
    overflow: hidden;
    box-shadow: 0 6px 18px rgba(0,0,0,.18);
  }
  .card--front { top: 100px; }
  .card--back { top: 531px; }

  .wordmark { color: var(--ink-grey); line-height: 1; }
  .wordmark__name { font-size: 44px; font-weight: 400; letter-spacing: 1px; display: block; }
  .wordmark__tag { font-size: 24px; font-weight: 400; letter-spacing: 8px; display: block; margin-top: 4px; }

  .card--front .wordmark { position: absolute; right: 70px; top: 70px; text-align: right; }
  .card--front .wordmark__url {
    display: block; margin-top: 10px;
    font-size: 14px; letter-spacing: 3px; color: var(--maroon);
  }

  .card--back .brand {
    position: absolute; left: 40px; top: 130px;
    display: flex; align-items: center; gap: 14px;
  }
  .brand__dot { width: 34px; height: 34px; border-radius: 50%; background: var(--maroon); flex: none; }

  .back-panel { position: absolute; inset: 0; width: 640px; height: 366px; }

  .contact {
    position: absolute; right: 26px; top: 52px;
    text-align: right; color: var(--white);
    font-size: 15px; line-height: 1.55;
  }
  .contact__name { color: var(--gold); font-size: 22px; font-weight: 700; line-height: 1.1; }
  .contact__creds { color: var(--gold); font-size: 14px; font-weight: 700; margin-bottom: 8px; }
  .contact__line { display: flex; justify-content: flex-end; align-items: center; gap: 6px; }
  .contact__line svg { width: 14px; height: 14px; flex: none; }
  .contact__place { margin-top: 8px; }
</style>
</head>
<body>
<main class="canvas">

  <section class="card card--front" aria-label="Card front">
    <div class="wordmark">
      <span class="wordmark__name">Quill Pond</span>
      <span class="wordmark__tag">consulting</span>
      <span class="wordmark__url">www.quillpond.example</span>
    </div>
  </section>

  <section class="card card--back" aria-label="Card back">
    <svg class="back-panel" viewBox="0 0 640 366" aria-hidden="true">
      <defs>
        <linearGradient id="panelTone" x1="0" y1="0" x2="1" y2="1">
          <stop offset="0" stop-color="#8a1d12"/>
          <stop offset="1" stop-color="#4e0e09"/>
        </linearGradient>
      </defs>
      <path d="M360 0 L640 0 L640 366 L300 366 Q330 180 360 0 Z" fill="url(#panelTone)"/>
    </svg>

    <div class="brand">
      <span class="brand__dot"></span>
      <div class="wordmark">
        <span class="wordmark__name">Quill Pond</span>
        <span class="wordmark__tag">consulting</span>
      </div>
    </div>

    <div class="contact">
      <p class="contact__name">Helen Marsh</p>
      <p class="contact__creds">B.Sc., M.Ed., PMP</p>
      <p class="contact__line">250.555.0184
        <svg viewBox="0 0 16 16" aria-hidden="true"><path d="M3 2h3l1 3-2 1a9 9 0 0 0 5 5l1-2 3 1v3a1 1 0 0 1-1 1A12 12 0 0 1 2 3a1 1 0 0 1 1-1z" fill="var(--gold)"/></svg>
      </p>
      <p class="contact__line">helen.marsh@quillpond.example
        <svg viewBox="0 0 16 16" aria-hidden="true"><rect x="1" y="3" width="14" height="10" fill="var(--gold)"/><path d="M1 3l7 6 7-6" fill="none" stroke="#4e0e09" stroke-width="1.2"/></svg>
      </p>
      <p class="contact__line">www.quillpond.example
        <svg viewBox="0 0 16 16" aria-hidden="true"><circle cx="8" cy="8" r="6.5" fill="var(--gold)"/><path d="M1.5 8h13M8 1.5c-3 3-3 10 0 13M8 1.5c3 3 3 10 0 13" fill="none" stroke="#4e0e09" stroke-width="1"/></svg>
      </p>
      <p class="contact__place">Fernhollow, Westmark, Canada</p>
    </div>
  </section>

</main>
</body>
</html>
```